Business cards and stationary design

We just completed the design of our new logo and we need to print new business cards and letterhead for our nonprofit. We are looking for a fresh new design that shows off our new logo. On letterhead, we must have a column on the right or left to include our Board of Directors (up to 45 names) (see attachment)

Industry/Entity Type

Non-Profit

Contact Information for Business Card

Standard business card with name, title, Company name, mailing address phone numbers, email address and website. Tagline on back "Bringing the homeless home"

Font styles to use
Sans Serif

Requirements
Must have
• include pertinent information above
• new logo
• fonts compatible with logo
• should use logo colors only
Nice to have
• tag lines

```html
<!DOCTYPE html>
<html lang="en">
<head>
<meta charset="utf-8">
<title>Shelter Path Alliance – Business Cards</title>
<link rel="stylesheet" href="https://fonts.googleapis.com/css2?family=Work+Sans:wght@400;600;700&display=swap">
<style>
  :root {
    --backdrop: #3a3734;
    --brand-red: #ed1c24;
    --brand-teal: #0e7e9e;
    --ink: #3b3b3b;
    --paper: #ffffff;
  }
  * { margin: 0; padding: 0; box-sizing: border-box; }
  html, body { width: 1200px; height: 930px; overflow: hidden; }
  body {
    background: var(--backdrop);
    font-family: "Work Sans", sans-serif;
    position: relative;
  }
  .card {
    position: absolute;
    width: 560px;
    height: 320px;
    border-radius: 16px;
    overflow: hidden;
    box-shadow: 0 10px 24px rgba(0,0,0,0.35);
  }
  .card--front {
    left: 80px; top: 90px;
    background: var(--brand-red);
    display: flex; align-items: center; justify-content: center;
  }
  .card--back {
    left: 560px; top: 520px;
    background: var(--paper);
  }
  .wordmark {
    display: flex; align-items: center; gap: 14px;
    font-weight: 600;
    font-size: 30px;
    letter-spacing: 3px;
    text-transform: uppercase;
    white-space: nowrap;
  }
  .wordmark__square { width: 26px; height: 26px; flex: none; }
  .card--front .wordmark { color: var(--paper); }
  .card--front .wordmark__square { background: var(--paper); }
  .card--back .wordmark {
    position: absolute; left: 40px; top: 126px;
    width: 250px;
    color: var(--brand-teal);
    font-size: 22px; letter-spacing: 2px; gap: 12px;
    line-height: 1.2;
  }
  .card--back .wordmark__square { background: var(--brand-teal); width: 22px; height: 22px; }
  .divider {
    position: absolute; left: 318px; top: 78px;
    width: 2px; height: 150px;
    background: var(--brand-teal);
  }
  .contact {
    position: absolute; left: 338px; top: 74px;
    color: var(--ink);
    font-size: 14px; line-height: 1.45;
  }
  .contact__name {
    color: var(--brand-teal);
    font-weight: 700; font-size: 22px;
    text-transform: uppercase; letter-spacing: 0.2px;
    line-height: 1.1;
  }
  .contact__title { margin-bottom: 6px; }
  .contact__address { margin-bottom: 4px; }
  .contact__line { display: flex; align-items: center; gap: 7px; }
  .contact__line svg { width: 10px; height: 10px; flex: none; }
  .stripe { position: absolute; bottom: 0; left: 0; width: 100%; height: 16px; }
</style>
</head>
<body>

  <section class="card card--front" aria-label="Card front">
    <div class="wordmark"><span class="wordmark__square"></span>Shelter Path Alliance</div>
  </section>

  <section class="card card--back" aria-label="Card back">
    <div class="wordmark"><span class="wordmark__square"></span><span>Shelter Path<br>Alliance</span></div>
    <div class="divider"></div>
    <div class="contact">
      <div class="contact__name">Daniel Reyes</div>
      <div class="contact__title">Director</div>
      <div class="contact__address">P.O. Box 52018,<br>Austin, Texas 78701</div>
      <div class="contact__line">
        <svg viewBox="0 0 10 10"><path d="M2 1 L4 1 L4.6 3 L3.4 3.8 Q4.4 5.8 6.2 6.6 L7 5.4 L9 6 L9 8 Q5 9.5 1.5 5 Q0.6 3 2 1 Z" fill="var(--brand-teal)"/></svg>
        512.555.0187
      </div>
      <div class="contact__line">
        <svg viewBox="0 0 10 10"><rect x="0.7" y="2" width="8.6" height="6" fill="none" stroke="var(--brand-teal)" stroke-width="1"/><path d="M0.7 2 L5 5.4 L9.3 2" fill="none" stroke="var(--brand-teal)" stroke-width="1"/></svg>
        info@shelterpath.org
      </div>
      <div class="contact__line">
        <svg viewBox="0 0 10 10"><circle cx="5" cy="5" r="4.2" fill="none" stroke="var(--brand-teal)" stroke-width="1"/><ellipse cx="5" cy="5" rx="1.8" ry="4.2" fill="none" stroke="var(--brand-teal)" stroke-width="0.8"/><line x1="0.8" y1="5" x2="9.2" y2="5" stroke="var(--brand-teal)" stroke-width="0.8"/></svg>
        www.shelterpath.org
      </div>
    </div>
    <svg class="stripe" viewBox="0 0 560 16" preserveAspectRatio="none">
      <polygon points="0,0 370,0 364,16 0,16" fill="var(--brand-teal)"/>
      <polygon points="376,0 560,0 560,16 370,16" fill="var(--brand-red)"/>
    </svg>
  </section>

</body>
</html>
```